Shop Window Desgin

I have a big glass window (office), 280cm wide by 302cm high and I want designing an advert for our property management business.

Our main colours are in the proeprty management logo attached. I have also uploaded a photo of the shop front (left window), please take into consideration the door.

I want the following text items placed:

PROPERTY MANAGEMENT
HOLIDAY RENTALS
KEYHOLDING
MARKETING & RESERVATIONS
GARDEN & POOL MAINTENACE
CLEANING & LAUNDRY

```html
<!DOCTYPE html>
<html lang="en">
<head>
<meta charset="utf-8">
<title>Harbourline Property Management – Shop Window</title>
<link rel="stylesheet" href="https://fonts.googleapis.com/css2?family=Bebas+Neue&family=Montserrat:wght@800&display=swap">
<style>
  :root {
    --orange: #e67e25;
    --grey: #808080;
    --white: #ffffff;
    --backdrop: #f1f1f1;
    --badge-blue: #1d9ad6;
    --badge-navy: #13305a;
    --badge-purple: #3e2c54;
  }
  * { margin: 0; padding: 0; box-sizing: border-box; }
  html, body { width: 1200px; height: 1013px; overflow: hidden; background: var(--backdrop); }
  .window-panel {
    position: absolute; left: 207px; top: 83px; width: 786px; height: 848px;
    background: var(--white);
  }
  .brand-square {
    position: absolute; left: 353px; top: 92px; width: 80px; height: 80px;
    background: var(--orange);
  }
  .brand-name {
    position: absolute; left: 0; width: 100%; top: 214px; text-align: center;
    font-family: "Montserrat", sans-serif; font-weight: 800; color: var(--orange);
    line-height: 1;
  }
  .brand-name .main { display: block; font-size: 58px; letter-spacing: 0.5px; }
  .brand-name .sub { display: block; font-size: 22px; margin-top: 10px; }
  .services-frame {
    position: absolute; left: 80px; top: 338px; width: 627px; height: 353px;
    border: 9px solid var(--grey); padding: 8px;
  }
  .services {
    width: 100%; height: 100%; background: var(--orange);
    position: relative;
  }
  .service {
    position: absolute; display: flex; align-items: center;
    font-family: "Bebas Neue", sans-serif; font-size: 31px; line-height: 33px;
    color: var(--white); letter-spacing: 0.3px;
  }
  .service-icon {
    width: 48px; height: 48px; border: 5px solid var(--white);
    margin-right: 26px; flex: none;
  }
  .col-left { left: 44px; }
  .col-right { left: 325px; }
  .row-1 { top: 42px; }
  .row-2 { top: 131px; }
  .row-3 { top: 220px; }
  .badges {
    position: absolute; top: 730px; left: 0; width: 100%; height: 80px;
  }
  .badge-pool {
    position: absolute; left: 216px; top: 6px; width: 68px; height: 68px;
    background: var(--badge-blue); border: 3px solid var(--badge-navy);
    border-radius: 12px; transform: rotate(45deg);
  }
  .badge-association {
    position: absolute; left: 339px; top: 10px; width: 247px; height: 60px;
    background: var(--badge-purple); border-radius: 6px;
  }
</style>
</head>
<body>
  <main class="window-panel">
    <div class="brand-square" aria-hidden="true"></div>
    <h1 class="brand-name">
      <span class="main">HARBOURLINE</span>
      <span class="sub">PROPERTY MANAGEMENT</span>
    </h1>

    <section class="services-frame">
      <ul class="services">
        <li class="service col-left row-1"><span class="service-icon"></span><span>Property.<br>Management</span></li>
        <li class="service col-left row-2"><span class="service-icon"></span><span>Holiday<br>Rentals</span></li>
        <li class="service col-left row-3"><span class="service-icon"></span><span>Key<br>Holding</span></li>
        <li class="service col-right row-1"><span class="service-icon"></span><span>Marketing &amp;<br>Reservations</span></li>
        <li class="service col-right row-2"><span class="service-icon"></span><span>Garden &amp;<br>Pool Maintenace</span></li>
        <li class="service col-right row-3"><span class="service-icon"></span><span>Cleaning &amp;<br>Laundry</span></li>
      </ul>
    </section>

    <div class="badges">
      <div class="badge-pool" role="img" aria-label="Pool and spa operator certification badge"></div>
      <div class="badge-association" role="img" aria-label="Vacation rental association membership badge"></div>
    </div>
  </main>
</body>
</html>
```